Brightpath Health Solutions

I need a professional and informational website for healthcare professionals. Please make the website the same style and content as our attached pdf.

Target Market(s)

Medical doctors

Industry/Entity Type

Healthcare

Coding

Coded - Design and coding required

Number of Pages Required

4 page

Requirements
Must have
• The same style and content as the uploaded powerpoints

```html
<!DOCTYPE html>
<html lang="en">
<head>
<meta charset="utf-8">
<title>Brightpath Health Solutions — Clinical Solutions</title>
<link href="https://fonts.googleapis.com/css2?family=Inter:wght@400;500;600&family=Plus+Jakarta+Sans:wght@500;600;700;800&display=swap" rel="stylesheet">
<style>
:root{
  --navy:#03112e;
  --navy-deep:#020b22;
  --ink:#0b1530;
  --body:#4a5366;
  --muted:#6b7385;
  --teal:#1a6e6e;
  --teal-dark:#145a5a;
  --cyan:#a9eef0;
  --tint:#e4f6f6;
  --page:#f7f8fa;
  --band:#eef0f3;
  --white:#ffffff;
  --line:#dfe3ea;
}
*{box-sizing:border-box;margin:0;padding:0}
html,body{width:1200px;height:2648px;overflow:hidden}
body{font-family:"Inter",sans-serif;color:var(--ink);background:var(--page)}
.display{font-family:"Plus Jakarta Sans",sans-serif}
.wrap{width:1024px;margin:0 auto;position:relative}

/* nav */
.nav{height:67px;background:var(--white);border-bottom:1px solid var(--line)}
.nav .wrap{height:100%;display:flex;align-items:center}
.brand{font-family:"Plus Jakarta Sans",sans-serif;font-weight:800;font-size:18px;line-height:1.05;color:var(--ink);letter-spacing:-.3px;width:150px}
.brand small{display:block;font-size:11px;font-weight:800;letter-spacing:.2px}
.menu{display:flex;gap:27px;margin-left:218px;font-size:12px;color:#3b4458}
.menu a{color:inherit;text-decoration:none;padding-bottom:4px}
.menu a.active{color:var(--teal);border-bottom:1.5px solid var(--teal)}
.btn-contact{margin-left:auto;background:var(--navy);color:#fff;font-size:12px;font-weight:500;padding:10px 17px;border-radius:2px}

/* hero */
.hero{height:455px;background:linear-gradient(135deg,#020a1e 0%,#03163a 60%,#062c55 100%);position:relative;overflow:hidden}
.hero .wrap{padding-top:79px}
.eyebrow{display:inline-block;background:#163e4e;color:var(--cyan);font-size:10px;font-weight:600;letter-spacing:.8px;padding:6px 10px;border-radius:2px}
.hero h1{font-family:"Plus Jakarta Sans",sans-serif;font-weight:800;font-size:50px;line-height:50px;letter-spacing:-1.8px;color:#fff;margin-top:22px}
.hero h1 span{color:var(--cyan)}
.hero p{color:#a9b4c8;font-size:15px;line-height:24px;margin-top:26px;width:560px}
.hero-actions{display:flex;gap:14px;margin-top:34px}
.btn{font-size:13px;font-weight:600;padding:15px 26px;border-radius:2px;color:#fff}
.btn-primary{background:var(--teal)}
.btn-ghost{border:1px solid #3a4a68;padding:14px 26px}
.hero-media{position:absolute;left:800px;top:46px;width:400px;height:363px;border-radius:22px 0 0 22px;background:linear-gradient(140deg,#13324a 0%,#1d4a5e 45%,#0c2236 100%)}

/* ecosystems */
.eco{height:659px;background:var(--page)}
.eco .wrap{padding-top:80px}
.section-title{font-family:"Plus Jakarta Sans",sans-serif;font-weight:800;font-size:25px;letter-spacing:-1.2px;color:var(--ink)}
.eco-head{display:flex;align-items:flex-end;justify-content:space-between;margin-left:4px}
.eco-lede{font-size:15px;line-height:23px;color:var(--body);margin-top:16px;width:560px}
.explore{font-size:12px;font-weight:600;color:var(--teal);display:flex;align-items:center;gap:6px;letter-spacing:-.2px;margin-bottom:2px;margin-right:-3px}
.cards{display:flex;gap:27px;margin-top:50px;margin-left:4px}
.card{width:322px;height:357px;background:var(--white);padding:33px 33px 0}
.card-icon{width:52px;height:52px;border-radius:4px;background:var(--tint);display:flex;align-items:center;justify-content:center}
.card h3{font-family:"Plus Jakarta Sans",sans-serif;font-weight:600;font-size:17px;margin-top:29px;letter-spacing:-.2px}
.card p{font-size:12px;line-height:19px;color:var(--body);margin-top:12px}
.card ul{list-style:none;margin-top:19px}
.card li{font-size:10.5px;font-weight:500;color:#2a3246;display:flex;align-items:center;gap:9px;height:23px}
.learn{display:block;font-size:10.5px;font-weight:600;letter-spacing:.9px;color:var(--teal);margin-top:37px}

/* workflow */
.workflow{height:666px;background:var(--band)}
.workflow .panel{position:absolute;left:88px;top:79px;width:1024px;height:508px;display:flex;border-radius:4px;overflow:hidden}
.wf-copy{width:512px;background:var(--white);padding:54px 53px 0}
.wf-copy h2{font-family:"Plus Jakarta Sans",sans-serif;font-weight:700;font-size:25px;line-height:30px;letter-spacing:-.8px}
.steps{margin-top:26px}
.step{display:flex;gap:19px;margin-bottom:33px}
.step-num{width:40px;height:40px;flex:none;border:1.5px solid var(--teal);border-radius:6px;display:flex;align-items:center;justify-content:center;font-family:"Plus Jakarta Sans",sans-serif;font-weight:700;font-size:13px;color:var(--teal)}
.step h4{font-family:"Plus Jakarta Sans",sans-serif;font-weight:600;font-size:15px;margin-top:1px}
.step p{font-size:12px;line-height:17px;color:var(--body);margin-top:8px;width:345px}
.wf-media{width:512px;position:relative;background:linear-gradient(160deg,#0f3040 0%,#0b2236 45%,#040f26 100%)}
.quote{position:absolute;left:40px;bottom:40px;width:420px}
.quote blockquote{font-size:16.5px;line-height:23px;color:#f1f4f8}
.quote cite{display:block;font-style:normal;font-size:10.5px;font-weight:600;letter-spacing:1.1px;color:var(--cyan);margin-top:15px}

/* standards */
.standards{height:403px;background:var(--page);text-align:center}
.standards .wrap{padding-top:78px}
.standards .section-title{font-size:30px;letter-spacing:-1.6px}
.rule{width:79px;height:3px;background:var(--teal);margin:14px auto 0}
.stats{display:flex;margin-top:63px}
.stat{width:264px}
.stat b{display:block;font-family:"Plus Jakarta Sans",sans-serif;font-weight:700;font-size:30px;letter-spacing:-.5px;color:var(--ink)}
.stat span{display:block;font-size:10.5px;font-weight:500;letter-spacing:1.4px;margin-top:6px;color:#2a3246}

/* footer */
.footer{height:398px;background:var(--navy-deep);color:#8c97ad}
.footer .wrap{padding-top:64px}
.foot-grid{display:flex}
.foot-col{width:268px}
.foot-col.about{width:268px}
.foot-brand{font-family:"Plus Jakarta Sans",sans-serif;font-weight:800;font-size:16px;line-height:1.05;color:#fff;letter-spacing:-.3px}
.foot-brand small{display:block;font-size:9px;font-weight:800}
.foot-col.about p{font-size:12px;line-height:19px;margin-top:24px;width:210px}
.socials{display:flex;gap:14px;margin-top:31px}
.socials span{width:32px;height:32px;border:1px solid #26304a;display:flex;align-items:center;justify-content:center}
.foot-col h5{font-size:10.5px;font-weight:600;letter-spacing:1.2px;color:var(--cyan);margin-top:1px}
.foot-col ul{list-style:none;margin-top:30px}
.foot-col li{font-size:12px;height:30px}
.foot-col .sub{font-size:12px;line-height:17px;margin-top:30px;width:205px}
.signup{display:flex;margin-top:17px;width:214px;height:24px}
.signup .field{flex:1;background:#0f1a33;font-size:12px;padding:5px 10px;color:#7b86a0}
.signup .send{width:42px;background:var(--teal);display:flex;align-items:center;justify-content:center}
.foot-bar{position:absolute;left:0;right:0;top:326px;border-top:1px solid #131d36;padding-top:32px;display:flex;font-size:9.5px;letter-spacing:1.1px;font-weight:500}
.foot-bar .legal{margin-left:auto;display:flex;gap:26px;color:#9aa6c0;font-weight:600}
</style>
</head>
<body>

<header class="nav">
  <div class="wrap">
    <div class="brand">Brightpath<small>Health Solutions</small></div>
    <nav class="menu">
      <a href="#">Home</a>
      <a href="#" class="active">Clinical Solutions</a>
      <a href="#">Patient Records</a>
      <a href="#">About Us</a>
    </nav>
    <span class="btn-contact">Contact</span>
  </div>
</header>

<section class="hero">
  <div class="wrap">
    <span class="eyebrow">PRECISION MEDICAL INFRASTRUCTURE</span>
    <h1>Clinical Solutions for the<br><span>Modern Practitioner</span></h1>
    <p>Harness the power of data-driven insights and integrated monitoring systems designed to elevate patient outcomes and streamline institutional workflows.</p>
    <div class="hero-actions">
      <span class="btn btn-primary">Request Demo</span>
      <span class="btn btn-ghost">View Documentation</span>
    </div>
  </div>
  <div class="hero-media" role="img" aria-label="Photo of a clinician's hand with a stylus over a tablet showing analytics charts"></div>
</section>

<section class="eco">
  <div class="wrap">
    <div class="eco-head">
      <div>
        <h2 class="section-title">SPECIALIZED CLINICAL ECOSYSTEMS</h2>
        <p class="eco-lede">Our suite of digital tools is engineered for high-stakes medical environments where speed, accuracy, and reliability are non-negotiable.</p>
      </div>
      <span class="explore">EXPLORE ALL SERVICES
        <svg width="14" height="14" viewBox="0 0 14 14" fill="none" stroke="currentColor" stroke-width="1.6"><path d="M1 7h11M8 3l4 4-4 4"/></svg>
      </span>
    </div>

    <div class="cards">
      <article class="card">
        <div class="card-icon">
          <svg width="20" height="20" viewBox="0 0 20 20" fill="none" stroke="#1a6e6e" stroke-width="1.6" stroke-linecap="round"><path d="M4 17h12M7 14h6M9 3l3 2-3 5-3-2zM12 9a4 4 0 0 1-2 6"/></svg>
        </div>
        <h3>Precision Diagnostics</h3>
        <p>AI-augmented pathology and radiology suites that provide diagnostic confidence with 99.8% accuracy rates in early detection.</p>
        <ul>
          <li><svg width="13" height="13" viewBox="0 0 13 13"><circle cx="6.5" cy="6.5" r="6.5" fill="#1a6e6e"/><path d="M3.8 6.6l1.8 1.8 3.6-3.6" stroke="#fff" stroke-width="1.4" fill="none"/></svg>Automated Pattern Recognition</li>
          <li><svg width="13" height="13" viewBox="0 0 13 13"><circle cx="6.5" cy="6.5" r="6.5" fill="#1a6e6e"/><path d="M3.8 6.6l1.8 1.8 3.6-3.6" stroke="#fff" stroke-width="1.4" fill="none"/></svg>High-Resolution Imaging</li>
        </ul>
        <span class="learn">LEARN MORE ›</span>
      </article>

      <article class="card">
        <div class="card-icon">
          <svg width="22" height="20" viewBox="0 0 22 20" fill="none" stroke="#1a6e6e" stroke-width="1.6" stroke-linejoin="round"><rect x="2" y="3" width="18" height="14" rx="1.5"/><path d="M4 10h4l2-3 2 6 2-3h4"/></svg>
        </div>
        <h3>Remote Patient Monitoring</h3>
        <p>Continuous telemetry that bridges the gap between the clinic and the home, ensuring patient safety through real-time vital tracking.</p>
        <ul>
          <li><svg width="13" height="13" viewBox="0 0 13 13"><circle cx="6.5" cy="6.5" r="6.5" fill="#1a6e6e"/><path d="M3.8 6.6l1.8 1.8 3.6-3.6" stroke="#fff" stroke-width="1.4" fill="none"/></svg>IoT Sensor Integration</li>
          <li><svg width="13" height="13" viewBox="0 0 13 13"><circle cx="6.5" cy="6.5" r="6.5" fill="#1a6e6e"/><path d="M3.8 6.6l1.8 1.8 3.6-3.6" stroke="#fff" stroke-width="1.4" fill="none"/></svg>Predictive Alert Systems</li>
        </ul>
        <span class="learn">LEARN MORE ›</span>
      </article>

      <article class="card">
        <div class="card-icon">
          <svg width="22" height="20" viewBox="0 0 22 20" fill="none" stroke="#1a6e6e" stroke-width="1.7" stroke-linecap="round"><path d="M2 13l4-5 3 3 5-7"/><circle cx="15" cy="13" r="3"/><path d="M17.2 15.2L20 18"/></svg>
        </div>
        <h3>Clinical Data Analytics</h3>
        <p>Convert raw clinical data into actionable population health insights with our proprietary deep-learning engine.</p>
        <ul>
          <li><svg width="13" height="13" viewBox="0 0 13 13"><circle cx="6.5" cy="6.5" r="6.5" fill="#1a6e6e"/><path d="M3.8 6.6l1.8 1.8 3.6-3.6" stroke="#fff" stroke-width="1.4" fill="none"/></svg>Trend Visualization</li>
          <li><svg width="13" height="13" viewBox="0 0 13 13"><circle cx="6.5" cy="6.5" r="6.5" fill="#1a6e6e"/><path d="M3.8 6.6l1.8 1.8 3.6-3.6" stroke="#fff" stroke-width="1.4" fill="none"/></svg>Outcome Benchmarking</li>
        </ul>
        <span class="learn">LEARN MORE ›</span>
      </article>
    </div>
  </div>
</section>

<section class="workflow" style="position:relative">
  <div class="panel">
    <div class="wf-copy">
      <h2>Interdisciplinary Workflow<br>Integration</h2>
      <div class="steps">
        <div class="step">
          <div class="step-num">01</div>
          <div><h4>Centralized Command Center</h4><p>Unify EHR, laboratory results, and imaging into a single clinical pane of glass.</p></div>
        </div>
        <div class="step">
          <div class="step-num">02</div>
          <div><h4>Evidence-Based Pathways</h4><p>Integrated decision support systems that align with global medical standards.</p></div>
        </div>
        <div class="step">
          <div class="step-num">03</div>
          <div><h4>Automated Documentation</h4><p>Natural language processing to reduce administrative burden on surgical teams.</p></div>
        </div>
      </div>
    </div>
    <div class="wf-media" role="img" aria-label="Photo of a surgeon in cap and mask working at a laptop in front of data displays">
      <div class="quote">
        <blockquote>"The predictive analytics module has reduced our readmission rates by 14% in the first quarter of implementation."</blockquote>
        <cite>DR. MARCUS HALE — CHIEF OF SURGERY</cite>
      </div>
    </div>
  </div>
</section>

<section class="standards">
  <div class="wrap">
    <h2 class="section-title">ENTERPRISE STANDARDS</h2>
    <div class="rule"></div>
    <div class="stats">
      <div class="stat"><b>99.9%</b><span>UPTIME RELIABILITY</span></div>
      <div class="stat"><b>HIPAA</b><span>COMPLIANT SECURITY</span></div>
      <div class="stat"><b>24/7</b><span>CLINICAL SUPPORT</span></div>
      <div class="stat"><b>150+</b><span>GLOBAL PARTNERS</span></div>
    </div>
  </div>
</section>

<footer class="footer">
  <div class="wrap">
    <div class="foot-grid">
      <div class="foot-col about">
        <div class="foot-brand">Brightpath<small>Health Solutions</small></div>
        <p>Pioneering the intersection of artificial intelligence and clinical excellence to reshape the future of patient care.</p>
        <div class="socials">
          <span><svg width="11" height="11" viewBox="0 0 12 12" fill="#c9d1e0"><circle cx="9" cy="2.5" r="1.8"/><circle cx="2.5" cy="6" r="1.8"/><circle cx="9" cy="9.5" r="1.8"/><path d="M3 6l6-3.5M3 6l6 3.5" stroke="#c9d1e0" stroke-width="1"/></svg></span>
          <span><svg width="11" height="11" viewBox="0 0 12 12" fill="none" stroke="#c9d1e0" stroke-width="1.2"><circle cx="6" cy="6" r="5"/><path d="M1 6h10M6 1c2 2 2 8 0 10M6 1c-2 2-2 8 0 10"/></svg></span>
        </div>
      </div>
      <div class="foot-col">
        <h5>SOLUTIONS</h5>
        <ul><li>Precision Diagnostics</li><li>Patient Monitoring</li><li>Clinical Analytics</li><li>Institutional ERP</li></ul>
      </div>
      <div class="foot-col">
        <h5>RESOURCES</h5>
        <ul><li>Clinical Whitepapers</li><li>API Documentation</li><li>Security Standards</li><li>Support Portal</li></ul>
      </div>
      <div class="foot-col">
        <h5>SUBSCRIBE</h5>
        <p class="sub">Receive clinical updates and industry news.</p>
        <div class="signup">
          <span class="field">Email address</span>
          <span class="send"><svg width="14" height="12" viewBox="0 0 14 12" fill="none" stroke="#fff" stroke-width="1.4" stroke-linejoin="round"><path d="M1 1l12 5-12 5 2-5z"/></svg></span>
        </div>
      </div>
    </div>
    <div class="foot-bar">
      <span>© 2024 BRIGHTPATH HEALTH SOLUTIONS. ALL CLINICAL RIGHTS RESERVED.</span>
      <span class="legal"><span>PRIVACY PROTOCOL</span><span>TERMS OF SERVICE</span><span>COOKIE POLICY</span></span>
    </div>
  </div>
</footer>

</body>
</html>
```